VM Tarlo Agency

we need a design for panel, cm 235 x 184 height + roll up as attached sizes, attached find also my logo, my company is www.vmtarloagency.com

Industry/Entity Type

Freight Forwarding

```html
<!DOCTYPE html>
<html lang="en">
<head>
<meta charset="utf-8">
<title>VM Tarlo Agency – Roll-up Banner</title>
<link href="https://fonts.googleapis.com/css2?family=Oswald:wght@500;700&family=Roboto+Condensed:wght@500&family=Exo+2:ital,wght@1,800&display=swap" rel="stylesheet">
<style>
  :root{
    --navy:#1b1f5c;
    --navy-deep:#141849;
    --red:#d8262b;
    --icon-red:#e3302d;
    --white:#ffffff;
    --paper:#f1f2f5;
  }
  html,body{margin:0;width:1200px;height:1200px;overflow:hidden;background:#e9ebef;}
  .banner{position:absolute;left:357px;top:30px;width:486px;height:1140px;overflow:hidden;background:var(--white);box-shadow:0 4px 18px rgba(0,0,0,.18);}
  .banner-shapes{position:absolute;inset:0;}
  .brand{position:absolute;left:0;right:0;top:104px;text-align:center;}
  .brand-mark{display:inline-flex;align-items:center;gap:10px;}
  .brand-dot{width:20px;height:20px;border-radius:50%;background:var(--navy);}
  .brand-name{font-family:'Oswald',sans-serif;font-weight:700;font-size:34px;color:var(--navy);letter-spacing:.2px;line-height:1;}
  .brand-tagline{margin-top:6px;font-family:'Roboto Condensed',sans-serif;font-weight:500;font-size:20px;color:var(--red);letter-spacing:1px;line-height:1.1;}
  .headline{position:absolute;left:0;right:0;top:196px;text-align:center;font-family:'Oswald',sans-serif;font-weight:700;font-size:40px;line-height:47px;color:var(--red);margin:0;letter-spacing:-.3px;}
  .services{position:absolute;left:0;right:0;top:618px;display:grid;grid-template-columns:1fr 1fr;row-gap:22px;margin:0;padding:0 8px;list-style:none;}
  .service{text-align:center;}
  .service svg{display:block;margin:0 auto 8px;height:84px;}
  .service-label{font-family:'Exo 2',sans-serif;font-style:italic;font-weight:800;font-size:24px;line-height:27px;color:var(--white);}
  .contact{position:absolute;left:0;right:0;top:958px;text-align:center;}
  .phone{font-family:'Oswald',sans-serif;font-weight:700;font-size:32px;color:var(--white);line-height:1;margin-top:4px;}
  .handle{font-family:'Exo 2',sans-serif;font-style:italic;font-weight:800;font-size:13px;color:var(--icon-red);margin-top:5px;display:flex;justify-content:center;align-items:center;gap:6px;}
  .handle-dot{width:7px;height:7px;border-radius:50%;background:var(--icon-red);}
  .cta{position:absolute;left:0;right:0;top:1066px;text-align:center;}
  .cta-line{font-family:'Exo 2',sans-serif;font-style:italic;font-weight:800;font-size:23px;color:var(--red);line-height:1;}
  .website{font-family:'Oswald',sans-serif;font-weight:700;font-size:29px;color:var(--navy);line-height:1.1;margin-top:2px;}
</style>
</head>
<body>
<div class="banner">
  <svg class="banner-shapes" viewBox="0 0 486 1140" width="486" height="1140">
    <defs>
      <linearGradient id="top-wash" x1="0" y1="0" x2="1" y2="1">
        <stop offset="0" stop-color="#e4e6ec"/><stop offset=".5" stop-color="#ffffff"/><stop offset="1" stop-color="#e8eaf0"/>
      </linearGradient>
      <linearGradient id="scene-fill" x1="0" y1="0" x2="0" y2="1">
        <stop offset="0" stop-color="#b7cfdf"/><stop offset=".45" stop-color="#e4eef3"/><stop offset=".75" stop-color="#c26a4f"/><stop offset="1" stop-color="#7e97ad"/>
      </linearGradient>
      <linearGradient id="navy-fill" x1="0" y1="0" x2="1" y2="1">
        <stop offset="0" stop-color="#1f2466"/><stop offset="1" stop-color="#141849"/>
      </linearGradient>
    </defs>
    <rect width="486" height="1140" fill="url(#top-wash)"/>
    <path d="M0 300 Q243 328 486 282 L486 290 Q243 336 0 308 Z" fill="var(--navy)"/>
    <path d="M0 306 Q243 334 486 288 L486 590 Q243 572 0 610 Z" fill="url(#scene-fill)" role="img" aria-label="Photo of cargo ship, freight train, cargo plane and truck in front of a world map and city skyline"/>
    <path d="M0 606 Q243 568 486 586 L486 596 Q243 578 0 616 Z" fill="var(--red)"/>
    <path d="M0 614 Q243 576 486 594 L486 1036 Q243 1056 0 1036 Z" fill="url(#navy-fill)"/>
    <path d="M0 614 L160 760 L0 900 Z M486 594 L330 700 L486 820 Z M140 1036 L243 900 L360 1044 Z" fill="#ffffff" opacity=".035"/>
    <rect y="1040" width="486" height="100" fill="var(--white)"/>
    <path d="M0 1036 Q243 1056 486 1036 L486 1046 Q243 1066 0 1046 Z" fill="var(--white)"/>
  </svg>

  <header class="brand">
    <div class="brand-mark"><span class="brand-dot"></span><span class="brand-name">VM TARLO AGENCY</span></div>
    <div class="brand-tagline">Shipping and Logistics</div>
  </header>

  <h1 class="headline">WE MAKE YOUR BUSINESS<br>FLOW CONTINOUSLY</h1>

  <ul class="services">
    <li class="service">
      <svg viewBox="0 0 100 84" fill="none" stroke="var(--icon-red)" stroke-width="3.5" stroke-linejoin="round" stroke-linecap="round">
        <path d="M10 24 L42 10 L72 22 L40 36 Z M10 24 L10 52 L40 66 L40 36 M72 22 L72 40"/>
        <path d="M24 18 L56 30"/>
        <path d="M58 64 L92 44 M64 52 L72 70 M74 50 L90 40 L94 44 L80 56 M62 58 L54 56"/>
      </svg>
      <div class="service-label">Freight<br>Forwarding</div>
    </li>
    <li class="service">
      <svg viewBox="0 0 100 84" fill="none" stroke="var(--icon-red)" stroke-width="3.5" stroke-linejoin="round">
        <path d="M8 80 L8 28 L50 6 L92 28 L92 80"/>
        <path d="M22 80 L22 40 L78 40 L78 80 M22 48 L78 48"/>
        <path d="M40 24 L60 24"/>
        <rect x="48" y="56" width="14" height="12"/><rect x="62" y="56" width="14" height="12"/><rect x="55" y="68" width="14" height="12"/>
      </svg>
      <div class="service-label">Warehouse<br>Logistics</div>
    </li>
    <li class="service">
      <svg viewBox="0 0 100 84" fill="none" stroke="var(--icon-red)" stroke-width="3.5" stroke-linejoin="round" stroke-linecap="round">
        <path d="M20 18 L54 8 L82 18 L82 48 L48 58 L20 48 Z M20 18 L48 28 L82 18 M48 28 L48 58"/>
        <path d="M8 66 L30 66 Q46 62 62 70 L88 64 Q94 66 88 72 L60 80 L8 78"/>
      </svg>
      <div class="service-label">Project<br>Cargoes</div>
    </li>
    <li class="service">
      <svg viewBox="0 0 130 84" fill="none" stroke="var(--icon-red)" stroke-width="3.5" stroke-linejoin="round">
        <rect x="4" y="30" width="34" height="34"/><rect x="44" y="30" width="34" height="34"/>
        <path d="M84 64 L84 38 L108 38 L122 50 L122 64 Z M96 46 L96 56 L112 56"/>
        <path d="M12 40 L30 40 M52 40 L70 40"/>
        <circle cx="14" cy="68" r="4"/><circle cx="30" cy="68" r="4"/><circle cx="54" cy="68" r="4"/><circle cx="70" cy="68" r="4"/><circle cx="94" cy="68" r="4"/><circle cx="114" cy="68" r="4"/>
      </svg>
      <div class="service-label">Rail<br>Services</div>
    </li>
  </ul>

  <section class="contact">
    <svg width="16" height="16" viewBox="0 0 24 24" fill="var(--icon-red)"><path d="M6.6 10.8a15 15 0 0 0 6.6 6.6l2.2-2.2a1 1 0 0 1 1-.25 11.4 11.4 0 0 0 3.6.57 1 1 0 0 1 1 1V20a1 1 0 0 1-1 1A17 17 0 0 1 3 4a1 1 0 0 1 1-1h3.5a1 1 0 0 1 1 1c0 1.25.2 2.450.57 3.57a1 1 0 0 1-.25 1z"/></svg>
    <div class="phone">+39 0255510473</div>
    <div class="handle"><span class="handle-dot"></span>@vmtarloagency.com</div>
  </section>

  <footer class="cta">
    <div class="cta-line">choose us!</div>
    <div class="website">www.vmtarloagency.com</div>
  </footer>
</div>
</body>
</html>
```